BrightLoop Kiosk Business Card Design Project

BrightLoop Kiosk requires a business card design. We hire PhotoBooths to events such as Birthday Parties, Hens and Bucks Night, Anniversaries, Corporate Functions
, Engagements, Theme Nights, Presentation Night etc.
Business Card needs to look Modern, Professional And Catchy.
Updates

Hello Thankyou for all of your great designs, contact information will be provided shortly. We are considering the front of the card to be white themed and the back of the card to be black themed. And all social media colours to be their original colour. Thankyou

Hello everyone, Here are the contact details: Martin Colby - Manager Mobile number - 0491738205 Website - www.brightloopkiosk.example Email - admin@brightloopkiosk.example And if you can add the word "weddings" in the "We cater For" section would be good. Thankyou

Target Market(s)

Birthday Parties
Hens and Bucks Night
Weddings
Corporate Functions
Engagements
Theme Nights
Presentation Night
School Functions

Industry/Entity Type

Events

Requirements
Must have
• Must Match Logo
Must Have www.brightloopkiosk.example

On Back of card must have social media icons Facebook, Twitter, Youtube, Linkin and

We Cater For:

Birthday Parties
Hens and Bucks Night
Anniversaries
Corporate Functions
Engagements
Theme Nights
Presentation Night
School Functions
And more.....

```html
<!DOCTYPE html>
<html lang="en">
<head>
<meta charset="utf-8">
<title>BrightLoop Kiosk – Business Card</title>
<link rel="stylesheet" href="https://fonts.googleapis.com/css2?family=Lato:wght@300;400;700;900&display=swap">
<style>
  :root {
    --page: #e6e7e9;
    --ink: #141414;
    --cyan: #23b4e3;
    --blue-light: #3cc1ee;
    --blue-mid: #1a7fc9;
    --blue-deep: #0d3f86;
    --white: #ffffff;
    --badge: #cdb48a;
  }
  * { box-sizing: border-box; margin: 0; padding: 0; }
  html, body { width: 1200px; height: 926px; overflow: hidden; }
  body {
    background: var(--page);
    font-family: "Lato", sans-serif;
    color: var(--ink);
    position: relative;
  }
  .card {
    position: absolute;
    left: 250px;
    width: 700px;
    height: 400px;
    overflow: hidden;
    box-shadow: 0 6px 18px rgba(0,0,0,.18);
  }

  /* Front */
  .card-front { top: 42px; background: var(--white); }
  .brand {
    position: absolute; top: 62px; left: 0; right: 0;
    display: flex; justify-content: center; align-items: center; gap: 16px;
  }
  .brand-mark { width: 46px; height: 46px; background: var(--cyan); }
  .brand-name {
    font-weight: 900; font-size: 44px; letter-spacing: 1px;
    color: var(--ink); text-transform: uppercase;
  }
  .divider {
    position: absolute; left: 0; right: 0; top: 168px;
    height: 2px; background: var(--cyan);
  }
  .person {
    position: absolute; top: 146px; left: 50%; transform: translateX(-50%);
    background: var(--white); padding: 0 14px; text-align: center;
  }
  .person-name {
    font-size: 38px; font-weight: 400; letter-spacing: .5px;
    text-transform: uppercase; line-height: 1.1; white-space: nowrap;
  }
  .person-name strong { font-weight: 900; }
  .person-role {
    font-size: 20px; color: var(--cyan); letter-spacing: 2px;
    text-transform: uppercase;
  }
  .contacts {
    position: absolute; top: 258px; left: 0; right: 0;
    list-style: none; display: flex; flex-direction: column; align-items: center; gap: 4px;
  }
  .contacts li { display: flex; align-items: center; gap: 10px; font-size: 22px; }
  .contacts svg { width: 20px; height: 20px; fill: none; stroke: var(--cyan); stroke-width: 2; }
  .band {
    position: absolute; left: 0; right: 0; bottom: 0; height: 18px; background: var(--cyan);
  }

  /* Back */
  .card-back {
    top: 484px;
    background: radial-gradient(ellipse at 55% 45%, var(--blue-light) 0%, var(--blue-mid) 45%, var(--blue-deep) 100%);
    color: var(--white);
  }
  .cater-title {
    position: absolute; top: 56px; left: 0; right: 0; text-align: center;
    font-weight: 900; font-size: 28px; letter-spacing: 1px; text-transform: uppercase;
  }
  .cater-list {
    position: absolute; list-style: none; font-size: 22px; line-height: 1.45;
  }
  .cater-list li { display: flex; align-items: center; gap: 12px; }
  .cater-list li::before {
    content: ""; width: 12px; height: 12px; border-radius: 50%; background: var(--white);
    flex: none;
  }
  .cater-left { top: 112px; left: 70px; }
  .cater-right { top: 112px; left: 430px; }
  .social {
    position: absolute; bottom: 40px; left: 0; right: 0;
    display: flex; justify-content: center; gap: 14px;
  }
  .social span { width: 30px; height: 30px; border-radius: 50%; background: var(--badge); }
</style>
</head>
<body>
  <section class="card card-front" aria-label="Card front">
    <div class="brand">
      <span class="brand-mark"></span>
      <span class="brand-name">BrightLoop Kiosk</span>
    </div>
    <div class="divider"></div>
    <div class="person">
      <p class="person-name">Martin <strong>Colby</strong></p>
      <p class="person-role">Manager</p>
    </div>
    <ul class="contacts">
      <li>
        <svg viewBox="0 0 20 20"><rect x="5" y="1.5" width="10" height="17" rx="2"/><line x1="9" y1="15.5" x2="11" y2="15.5"/></svg>
        0491 738 205
      </li>
      <li>
        <svg viewBox="0 0 20 20"><rect x="1.5" y="3" width="17" height="11" rx="1"/><line x1="7" y1="17.5" x2="13" y2="17.5"/><line x1="10" y1="14" x2="10" y2="17.5"/></svg>
        www.brightloopkiosk.example
      </li>
      <li>
        <svg viewBox="0 0 20 20"><rect x="1.5" y="4" width="17" height="12" rx="1"/><polyline points="1.5,4 10,11 18.5,4"/></svg>
        admin@brightloopkiosk.example
      </li>
    </ul>
    <div class="band"></div>
  </section>

  <section class="card card-back" aria-label="Card back">
    <h2 class="cater-title">We Cater For</h2>
    <ul class="cater-list cater-left">
      <li>Birthday Parties</li>
      <li>Hens and Bucks Night</li>
      <li>Anniversaries</li>
      <li>Corporate Functions</li>
      <li>Engagements</li>
    </ul>
    <ul class="cater-list cater-right">
      <li>Theme Nights</li>
      <li>Presentation Night</li>
      <li>School Functions</li>
      <li>Weddings</li>
      <li>And more.....</li>
    </ul>
    <div class="social" aria-label="Social media links">
      <span></span><span></span><span></span><span></span>
    </div>
  </section>
</body>
</html>
```